Full service facility management

Stationery Branding needed for Envelopes, folders, letterheads to show the services we offer (valet, security, front desk/concierge, janitorial, maintenance services to CONDOMINIUMS). We need the our logo and colors to be branded to these items

Target Market(s)

Homeowner Condominiums / High Rise residential living

Font styles to use
Sans Serif

Colors
0355a3

```html
<!DOCTYPE html>
<html lang="en">
<head>
<meta charset="utf-8">
<title>Halvern Estates Inc. – Envelope</title>
<link href="https://fonts.googleapis.com/css2?family=Open+Sans:wght@400;600&display=swap" rel="stylesheet">
<style>
  :root {
    --backdrop: #c9cbce;
    --paper: #f7f7f7;
    --ink: #111111;
    --ink-soft: #333333;
  }
  html, body {
    margin: 0;
    width: 1200px;
    height: 834px;
    overflow: hidden;
    background: var(--backdrop);
    font-family: "Open Sans", sans-serif;
  }
  .envelope {
    position: absolute;
    left: 100px;
    top: 182px;
    width: 1000px;
    height: 470px;
    background: var(--paper);
    overflow: hidden;
  }
  .brand {
    position: absolute;
    left: 56px;
    top: 120px;
  }
  .brand-mark {
    width: 96px;
    height: 96px;
    background: var(--ink);
    margin-bottom: 14px;
  }
  .brand-name {
    font-size: 26px;
    font-weight: 400;
    color: var(--ink);
    margin: 0;
    line-height: 1.1;
  }
  .brand-tagline {
    font-size: 15px;
    color: var(--ink-soft);
    margin: 4px 0 0;
  }
  .corner-stripes {
    position: absolute;
    right: 0;
    top: 250px;
  }
  .services {
    position: absolute;
    left: 56px;
    right: 120px;
    top: 352px;
    display: flex;
    justify-content: space-between;
    align-items: center;
    list-style: none;
    margin: 0;
    padding: 0;
  }
  .service {
    display: flex;
    align-items: center;
    gap: 7px;
    font-size: 10px;
    text-transform: uppercase;
    color: var(--ink);
    line-height: 1.2;
    letter-spacing: 0.02em;
    white-space: nowrap;
  }
  .service svg { width: 18px; height: 18px; fill: var(--ink); flex: none; }
  .rule-thin {
    position: absolute;
    left: 0; right: 0;
    top: 392px;
    height: 5px;
    background: var(--ink);
  }
  .band {
    position: absolute;
    left: 0; right: 0;
    top: 408px;
    bottom: 0;
    background: var(--ink);
  }
</style>
</head>
<body>
  <main class="envelope">
    <div class="brand">
      <div class="brand-mark"></div>
      <h1 class="brand-name">Halvern Estates Inc.</h1>
      <p class="brand-tagline">Facilities Management Services</p>
    </div>

    <svg class="corner-stripes" width="70" height="142" viewBox="0 0 70 142" aria-hidden="true">
      <polygon points="46,0 56,0 14,142 4,142" fill="#111"/>
      <polygon points="60,0 70,0 70,12 32,142 22,142" fill="#111"/>
      <polygon points="70,46 70,80 52,142 40,142" fill="#111"/>
    </svg>

    <ul class="services">
      <li class="service">
        <svg viewBox="0 0 20 20"><circle cx="10" cy="5" r="4"/><path d="M2 19c0-5 3.5-8 8-8s8 3 8 8z"/></svg>
        <span>Valet Parking Services</span>
      </li>
      <li class="service">
        <svg viewBox="0 0 20 20"><path d="M10 1l8 3v6c0 5-4 8-8 9-4-1-8-4-8-9V4z"/></svg>
        <span>Access Control<br>and Security Services</span>
      </li>
      <li class="service">
        <svg viewBox="0 0 20 20"><path d="M3 15a7 7 0 0 1 14 0z"/><rect x="1" y="16" width="18" height="2"/><circle cx="10" cy="6" r="1.5"/></svg>
        <span>Front Desk Services</span>
      </li>
      <li class="service">
        <svg viewBox="0 0 20 20"><rect x="9" y="1" width="2" height="11"/><path d="M4 11h12l-2 8H6z"/></svg>
        <span>Janitorial Services</span>
      </li>
      <li class="service">
        <svg viewBox="0 0 20 20"><rect x="2" y="7" width="6" height="12"/><rect x="9" y="2" width="9" height="17"/></svg>
        <span>Building Engineering</span>
      </li>
    </ul>

    <div class="rule-thin"></div>
    <div class="band"></div>
  </main>
</body>
</html>
```